Construction Company Business Card & Stationary
Brovella Concrete
Construction Company Business Card & Stationary - Construction
Creative Brief
Professional
MARCUS DELWYN JR.
Owner
P.O. Box 482 913 Tamsworth Ridge Lane Medford, NJ 08067
MarcusJr@Brovella.com
www.Brovella.com

```html
<!DOCTYPE html>
<html lang="en">
<head>
<meta charset="utf-8">
<title>Brovella Concrete Business Card</title>
<link href="https://fonts.googleapis.com/css2?family=Arimo:wght@400;700&display=swap" rel="stylesheet">
<style>
  :root {
    --backdrop: #e4e5e7;
    --card: #ffffff;
    --ink: #141414;
    --ink-soft: #3a3a3a;
    --rule: #141414;
    --shadow: rgba(0,0,0,0.16);
  }
  html, body {
    margin: 0; padding: 0;
    width: 1200px; height: 901px;
    overflow: hidden;
    background: var(--backdrop);
    font-family: "Arimo", Arial, sans-serif;
    color: var(--ink);
  }
  .canvas { position: relative; width: 1200px; height: 901px; }
  .card {
    position: absolute;
    width: 520px; height: 297px;
    background: var(--card);
    box-shadow: 0 10px 28px var(--shadow);
    box-sizing: border-box;
  }
  .card-front { left: 50px; top: 302px; }
  .card-back { left: 630px; top: 302px; }

  .brand { position: absolute; display: flex; align-items: center; }
  .brand-mark { background: var(--ink); flex: none; }
  .brand-name {
    font-weight: 700;
    letter-spacing: 1px;
    line-height: 1;
    white-space: nowrap;
    text-transform: uppercase;
  }
  .brand-tagline {
    position: absolute;
    font-weight: 400;
    text-transform: uppercase;
    white-space: nowrap;
    color: var(--ink-soft);
  }

  .card-front .brand { left: 62px; top: 112px; gap: 14px; }
  .card-front .brand-mark { width: 22px; height: 22px; }
  .card-front .brand-name { font-size: 34px; }
  .card-front .brand-tagline { left: 62px; top: 162px; font-size: 11px; letter-spacing: 2.6px; }
  .website { position: absolute; font-size: 15px; }
  .card-front .website { right: 40px; bottom: 32px; }

  .card-back .brand { left: 34px; top: 62px; gap: 9px; }
  .card-back .brand-mark { width: 14px; height: 14px; }
  .card-back .brand-name { font-size: 22px; }
  .card-back .brand-tagline { left: 34px; top: 96px; font-size: 7.5px; letter-spacing: 1.6px; }
  .card-back .website { right: 26px; top: 22px; font-size: 11px; }
  .divider { position: absolute; left: 34px; top: 150px; width: 200px; height: 3px; background: var(--rule); }
  .person { position: absolute; left: 34px; top: 166px; font-size: 11px; line-height: 1.4; }
  .person-name { font-weight: 700; font-size: 12px; letter-spacing: 0.5px; }
  .person-role { margin-bottom: 12px; color: var(--ink-soft); }
  .contact { position: absolute; left: 320px; top: 150px; font-size: 11px; list-style: none; margin: 0; padding: 0; }
  .contact li { display: flex; align-items: center; gap: 8px; height: 18px; white-space: nowrap; }
  .contact svg { width: 10px; height: 10px; fill: var(--ink); flex: none; }
</style>
</head>
<body>
<div class="canvas">
  <section class="card card-front">
    <div class="brand">
      <span class="brand-mark"></span>
      <span class="brand-name">Brovella Concrete</span>
    </div>
    <div class="brand-tagline">Solid work from the ground up</div>
    <div class="website">www.Brovella.com</div>
  </section>

  <section class="card card-back">
    <div class="website">www.Brovella.com</div>
    <div class="brand">
      <span class="brand-mark"></span>
      <span class="brand-name">Brovella Concrete</span>
    </div>
    <div class="brand-tagline">Solid work from the ground up</div>
    <div class="divider"></div>
    <div class="person">
      <div class="person-name">MARCUS DELWYN JR.</div>
      <div class="person-role">Owner</div>
      <div>P.O. Box 482</div>
      <div>913 Tamsworth Ridge Lane</div>
      <div>Kestrel Falls, OR 97215</div>
    </div>
    <ul class="contact">
      <li><svg viewBox="0 0 10 10"><path d="M2 0.5 L3.6 0.5 L4.2 3 L3 3.8 Q4 6 6.2 7 L7 5.8 L9.5 6.4 L9.5 8 Q9.5 9.5 8 9.5 Q0.5 9 0.5 2 Q0.5 0.5 2 0.5Z"/></svg>609-555-0142</li>
      <li><svg viewBox="0 0 10 10"><rect x="2.5" y="0.5" width="5" height="9" rx="1"/></svg>609-555-0187</li>
      <li><svg viewBox="0 0 10 10"><rect x="0.5" y="3" width="9" height="6"/><rect x="2.5" y="0.5" width="5" height="3"/></svg>609-555-0163</li>
      <li><svg viewBox="0 0 10 10"><path d="M0.5 2 H9.5 V8.5 H0.5Z M1 2.5 L5 5.5 L9 2.5" stroke="#fff" stroke-width="0.8"/></svg>MarcusJr@Brovella.com</li>
    </ul>
  </section>
</div>
</body>
</html>
```